Van Signwriting Design - Part Wrap - Battery Company

We would like some van wrap designs for 3 of our vans. The design is to be the same but needs to work on 3 different size vans - Fiat Ducato L1H2 2015, Ford Transit Connect 240 LWB 2015 , Ford Transit Custom L1H1 2017.
I would like it a part wrap design, so the front and front parts of the side of the vans remain white, with the middle to back sides and back where the design will be.
I would like our logo to be prominent on the sides but also have our website and pictures of batteries.
On the rear the pictures can be prominent and the logo smaller.
The website address www.voltarigo.com should be on the sides and rear along with our main telephone number 01632 457093.
I am open to colours but it should match the logo and remain professional and eye catching.
I have attached the logosand some pictures of the batteries. We can have the pictures redone if necessary to fill a space correctly.
If you can add the following that would also be great
BATTERIES - CABLES - ACCESSORIES
AUTOMOTIVE - INDUSTRIAL - SPECIALIST

Industry/Entity Type

Battery

Font styles to use
Sans Serif

Requirements
Must have
• Prominent Logo on the sides. - The rear can have a prominent battery images and a smaller logo.
Battery Images - We can redo these as required - for example to feature 3 batteries together stacked in a triangle or from different angles etc. Whatever works with the available space/design.
Website address - www.voltarigo.com
Telephone - 01632 457093
Bold, attractive easy to read design
Nice to have
• Text - "Automotive - Industrial - Specialist "
Text - "Batteries - Cables - Accessories"

```html
<!DOCTYPE html>
<html lang="en">
<head>
<meta charset="utf-8">
<title>Voltarigo Power Solutions – Van Part Wrap</title>
<link rel="stylesheet" href="https://fonts.googleapis.com/css2?family=Oswald:wght@500;700&display=swap">
<style>
  :root {
    --brand-blue: #1646a0;
    --brand-blue-deep: #0b2a6e;
    --brand-blue-light: #2f7ad6;
    --brand-red: #d4202a;
    --panel-white: #ffffff;
    --panel-edge: #d9dde3;
    --battery-dark: #1d2126;
    --battery-copper: #8a5a2b;
    --page: #ffffff;
  }
  html, body {
    margin: 0;
    padding: 0;
    width: 1200px;
    height: 1200px;
    overflow: hidden;
    background: var(--page);
  }
  .canvas {
    position: relative;
    width: 1200px;
    height: 1200px;
  }
  .wrap-panel {
    position: absolute;
    display: block;
  }
  .wrap-panel--large { left: 100px; top: 110px; width: 1000px; height: 380px; }
  .wrap-panel--small { left: 100px; top: 650px; width: 860px; height: 327px; }
  .panel-body { fill: var(--panel-white); stroke: var(--panel-edge); stroke-width: 2; }
  .brand-name {
    font-family: "Oswald", sans-serif;
    font-weight: 700;
    font-size: 92px;
    letter-spacing: 2px;
    fill: var(--brand-blue);
  }
  .brand-rule { fill: var(--brand-red); }
  .brand-tagline {
    font-family: "Oswald", sans-serif;
    font-weight: 700;
    font-size: 38px;
    letter-spacing: 1px;
    fill: var(--brand-red);
  }
  .service-band { fill: var(--brand-red); }
  .service-list {
    font-family: "Oswald", sans-serif;
    font-weight: 500;
    font-size: 15px;
    letter-spacing: 0.5px;
    fill: var(--panel-white);
  }
  .phone {
    font-family: "Oswald", sans-serif;
    font-weight: 500;
    font-size: 30px;
    letter-spacing: 1px;
    fill: var(--brand-red);
  }
  .website {
    font-family: "Oswald", sans-serif;
    font-weight: 700;
    font-size: 18px;
    fill: var(--brand-blue);
  }
</style>
</head>
<body>
<main class="canvas">

  <svg class="wrap-panel wrap-panel--large" viewBox="0 0 1000 380" xmlns="http://www.w3.org/2000/svg">
    <defs>
      <linearGradient id="energyBlue" x1="0" y1="0" x2="1" y2="1">
        <stop offset="0" stop-color="var(--brand-blue-light)"/>
        <stop offset="0.5" stop-color="var(--brand-blue)"/>
        <stop offset="1" stop-color="var(--brand-blue-deep)"/>
      </linearGradient>
      <linearGradient id="batteryDark" x1="0" y1="0" x2="0" y2="1">
        <stop offset="0" stop-color="#3a4048"/>
        <stop offset="1" stop-color="var(--battery-dark)"/>
      </linearGradient>
      <linearGradient id="batteryCopper" x1="0" y1="0" x2="0" y2="1">
        <stop offset="0" stop-color="#b07a44"/>
        <stop offset="1" stop-color="var(--battery-copper)"/>
      </linearGradient>
    </defs>
    <rect class="panel-body" x="1" y="1" width="998" height="378" rx="18"/>
    <path class="energy-field" role="img" aria-label="Blue field with electric lightning streaks"
          fill="url(#energyBlue)" d="M2,205 L555,198 Q585,198 600,222 L690,378 L2,378 Z"/>
    <path class="service-band" d="M2,162 L575,152 Q610,152 628,190 L730,378 L690,378 L600,222 Q585,198 555,198 L2,205 Z"/>
    <text class="brand-name" x="36" y="96">VOLTARIGO</text>
    <rect class="brand-rule" x="36" y="104" width="470" height="7"/>
    <text class="brand-tagline" x="36" y="146">POWER SOLUTIONS</text>
    <text class="service-list" x="24" y="186">• BATTERIES  • CABLES  • ACCESSORIES  • AUTOMOTIVE  • INDUSTRIAL  • SPECIALIST</text>
    <rect role="img" aria-label="Photo of a black car battery" x="26" y="222" width="96" height="84" rx="4" fill="url(#batteryDark)"/>
    <rect role="img" aria-label="Photo of a copper and black car battery" x="112" y="244" width="108" height="86" rx="4" fill="url(#batteryCopper)"/>
    <text class="phone" x="770" y="232">01632 457093</text>
    <text class="website" x="770" y="258">www.voltarigo.com</text>
  </svg>

  <svg class="wrap-panel wrap-panel--small" viewBox="0 0 1000 380" xmlns="http://www.w3.org/2000/svg">
    <defs>
      <linearGradient id="energyBlueSmall" x1="0" y1="0" x2="1" y2="1">
        <stop offset="0" stop-color="var(--brand-blue-light)"/>
        <stop offset="0.5" stop-color="var(--brand-blue)"/>
        <stop offset="1" stop-color="var(--brand-blue-deep)"/>
      </linearGradient>
      <linearGradient id="batteryDarkSmall" x1="0" y1="0" x2="0" y2="1">
        <stop offset="0" stop-color="#3a4048"/>
        <stop offset="1" stop-color="var(--battery-dark)"/>
      </linearGradient>
      <linearGradient id="batteryCopperSmall" x1="0" y1="0" x2="0" y2="1">
        <stop offset="0" stop-color="#b07a44"/>
        <stop offset="1" stop-color="var(--battery-copper)"/>
      </linearGradient>
    </defs>
    <rect class="panel-body" x="1" y="1" width="998" height="378" rx="18"/>
    <path class="energy-field" role="img" aria-label="Blue field with electric lightning streaks"
          fill="url(#energyBlueSmall)" d="M2,205 L555,198 Q585,198 600,222 L690,378 L2,378 Z"/>
    <path class="service-band" d="M2,162 L575,152 Q610,152 628,190 L730,378 L690,378 L600,222 Q585,198 555,198 L2,205 Z"/>
    <text class="brand-name" x="36" y="96">VOLTARIGO</text>
    <rect class="brand-rule" x="36" y="104" width="470" height="7"/>
    <text class="brand-tagline" x="36" y="146">POWER SOLUTIONS</text>
    <text class="service-list" x="24" y="186">• BATTERIES  • CABLES  • ACCESSORIES  • AUTOMOTIVE  • INDUSTRIAL  • SPECIALIST</text>
    <rect role="img" aria-label="Photo of a black car battery" x="26" y="222" width="96" height="84" rx="4" fill="url(#batteryDarkSmall)"/>
    <rect role="img" aria-label="Photo of a copper and black car battery" x="112" y="244" width="108" height="86" rx="4" fill="url(#batteryCopperSmall)"/>
    <text class="phone" x="770" y="232">01632 457093</text>
    <text class="website" x="770" y="258">www.voltarigo.com</text>
  </svg>

</main>
</body>
</html>
```